VORN Paradigm. the way you communicate in every situation and in all environments.

I would like you to create a diagram depicting a very specific process of communication. it must follow the look of the diagram that i have attached. this is going to be used in a book called LANTERN. it is going to explain the fact that we communicate all the same way using this process as we communicate. it starts with the fact that everyone takes everything that is said personally and then moves on to filters, which is your own agenda or experience kicking in. then you move to your why it matters, which is your motivation and ends with the choice of words you use when you communicate. if you are going to be successful then you must separate the person from the issue.

Target Market(s)

market is executive business people around the world

Industry/Entity Type

Consulting

Font styles to use
Sans Serif

Colors

Designer to choose only greyscale colors for use in the design.

Requirements
Must have
• I would like it to have a diving/ocean/snorkel feel to it. The analogy we are using is to make a deep dive when you are communicating. it must have every part of the diagram you see, it starts at the top with the vorn paradigm (and the words) it then connects to the filters which connects to the why it matters with connects to the words and then end with the separating the person from the issue.
Nice to have
• we are writing a black and white book NO color. therefore the words should be clear and easy to read. Each section should be able to stand on its own so we can write about it separately.
Should not have
• the diagram DOES NOT have to look like the one i gave you. it must explain the fact that it starts with VORN and ends with Separate and must pass through the three areas to get to the SEPARATE.

```html
<!DOCTYPE html>
<html lang="en">
<head>
<meta charset="utf-8">
<title>VORN Paradigm – Communication Process</title>
<link href="https://fonts.googleapis.com/css2?family=Montserrat:wght@500;700&display=swap" rel="stylesheet">
<style>
  :root {
    --paper: #ffffff;
    --ring: #909194;
    --ring-dark: #85868a;
    --disc-top: #ffffff;
    --disc-bottom: #e4e4e5;
    --ink: #1d1d1f;
    --rule: #3a3a3c;
    --arrow-light: #f2f2f2;
    --arrow-dark: #9c9da0;
  }
  html, body {
    margin: 0;
    padding: 0;
    width: 1200px;
    height: 1200px;
    overflow: hidden;
    background: var(--paper);
  }
  .diagram {
    position: relative;
    width: 1200px;
    height: 1200px;
    font-family: "Montserrat", Arial, sans-serif;
    color: var(--ink);
  }
  .diagram__art {
    position: absolute;
    inset: 0;
  }
  .node {
    position: absolute;
    width: 230px;
    height: 230px;
    margin: -115px 0 0 -115px;
    display: flex;
    flex-direction: column;
    align-items: center;
    justify-content: center;
    text-align: center;
  }
  .node__title {
    margin: 0;
    font-weight: 700;
    font-size: 22.5px;
    line-height: 29px;
    letter-spacing: 0.3px;
    text-transform: uppercase;
  }
  .node__rule {
    width: 180px;
    height: 0;
    border: 0;
    border-top: 1.2px solid var(--rule);
    margin: 8px 0 10px;
  }
  .node__text {
    margin: 0;
    font-weight: 500;
    font-size: 17.5px;
    line-height: 25px;
  }
  .node--start  { left: 603px; top: 275px; }
  .node--filters{ left: 272px; top: 607px; }
  .node--why    { left: 603px; top: 607px; }
  .node--words  { left: 935px; top: 607px; }
  .node--end    { left: 603px; top: 938px; }
</style>
</head>
<body>
<main class="diagram">
  <svg class="diagram__art" width="1200" height="1200" viewBox="0 0 1200 1200" aria-hidden="true">
    <defs>
      <linearGradient id="disc-fill" x1="0" y1="0" x2="0" y2="1">
        <stop offset="0" stop-color="var(--disc-top)"/>
        <stop offset="0.55" stop-color="#f7f7f7"/>
        <stop offset="1" stop-color="var(--disc-bottom)"/>
      </linearGradient>
      <linearGradient id="flow-in" x1="466" y1="300" x2="304" y2="458" gradientUnits="userSpaceOnUse">
        <stop offset="0" stop-color="var(--arrow-light)"/>
        <stop offset="1" stop-color="var(--arrow-dark)"/>
      </linearGradient>
      <linearGradient id="flow-out" x1="912" y1="745" x2="752" y2="900" gradientUnits="userSpaceOnUse">
        <stop offset="0" stop-color="var(--arrow-light)"/>
        <stop offset="1" stop-color="var(--arrow-dark)"/>
      </linearGradient>
      <linearGradient id="step-arrow" x1="0" y1="0" x2="1" y2="0">
        <stop offset="0" stop-color="#e9e9ea"/>
        <stop offset="1" stop-color="#ffffff"/>
      </linearGradient>
      <filter id="disc-shadow" x="-20%" y="-20%" width="140%" height="140%">
        <feDropShadow dx="0" dy="3" stdDeviation="4" flood-color="#000" flood-opacity="0.28"/>
      </filter>
    </defs>

    <!-- curved flow arrows -->
    <g class="flow">
      <path d="M466 300 Q385 330 331 410" fill="none" stroke="url(#flow-in)" stroke-width="30"/>
      <polygon points="304,458 292,398 362,432" fill="var(--arrow-dark)"/>
      <path d="M912 745 Q885 830 800 880" fill="none" stroke="url(#flow-out)" stroke-width="30"/>
      <polygon points="752,900 770,852 828,910" fill="var(--arrow-dark)"/>
    </g>

    <!-- bridges between the middle row -->
    <g class="bridge" fill="var(--ring)">
      <path d="M400 560 Q437 588 475 560 L475 646 Q437 618 400 646 Z"/>
      <path d="M731 560 Q768 588 806 560 L806 646 Q768 618 731 646 Z"/>
    </g>

    <!-- rings -->
    <g class="ring" fill="var(--ring)">
      <circle cx="603" cy="271" r="144"/>
      <circle cx="272" cy="603" r="144"/>
      <circle cx="603" cy="603" r="144"/>
      <circle cx="935" cy="603" r="144"/>
      <circle cx="603" cy="935" r="144"/>
    </g>

    <!-- step arrows -->
    <g class="step-arrow" fill="url(#step-arrow)">
      <polygon points="399,590 430,590 430,578 463,603 430,628 430,616 399,616"/>
      <polygon points="730,590 761,590 761,578 794,603 761,628 761,616 730,616"/>
    </g>

    <!-- discs -->
    <g class="disc" fill="url(#disc-fill)" filter="url(#disc-shadow)">
      <circle cx="603" cy="271" r="123"/>
      <circle cx="272" cy="603" r="123"/>
      <circle cx="603" cy="603" r="123"/>
      <circle cx="935" cy="603" r="123"/>
      <circle cx="603" cy="935" r="123"/>
    </g>
  </svg>

  <section class="node node--start">
    <h2 class="node__title">VORN<br>Paradigm</h2>
    <hr class="node__rule">
    <p class="node__text">When words are<br>taken personally,<br>what happens?</p>
  </section>

  <section class="node node--filters">
    <h2 class="node__title">Your<br>Filters</h2>
    <hr class="node__rule">
    <p class="node__text">An accumulation<br>of your experience,<br>knowledge and<br>values</p>
  </section>

  <section class="node node--why">
    <h2 class="node__title">Why It<br>Matters</h2>
    <hr class="node__rule">
    <p class="node__text">This is your<br>compass. It is what<br>motivates you, what<br>drives you.</p>
  </section>

  <section class="node node--words">
    <h2 class="node__title">Your<br>Words</h2>
    <hr class="node__rule">
    <p class="node__text">This is your<br>immediate response,<br>verbal or perhaps<br>non-verbal</p>
  </section>

  <section class="node node--end">
    <h2 class="node__title">What<br>To Do</h2>
    <hr class="node__rule">
    <p class="node__text">Separate the<br>Person from<br>the Issue</p>
  </section>
</main>
</body>
</html>
```